Business Card and Letterhead for new company Vardel GreenWorks, Inc.

Vardel GreenWorks, Inc., an engineering and construction firm that provides services for solid waste landfill gas systems, needs a business card and letterhead. We recently had a logo designed but we are open to some tweaks to logo design and color scheme. Generally, we like "earthy" color tones - greens, browns, oranges. This is a sister company - www.talvoriengineering.example.

Target Market(s)

Solid waste landfill companies - Brindle Disposal, Halcott Hauling, etc.

Industry/Entity Type

Engineering and Construction

Contact Information for Business Card

Name, Title, email, mobile phone, work phone, website. Potential list of services for back of card: LFG Engineering and Design, GCCS Planning and Operational Consulting, Compliance Monitoring and Reporting, Routine Operations & Maintenance, Nonroutine O&M, Construction Management, Construction QA, GCCS Construction

Font styles to use
Sans Serif

Requirements
Must have
• Logo, pertinent information, maybe a tagline (still in development)
Nice to have
• For back of card, considering an engineering scale (attached for another business of ours), but want to look at other options, alternatives. Like the idea of the back of card to have some utility (scale, unit conversion info, list of services) but willing to consider lots of options.
Should not have
• Needs to have a professional (engineering) and technical look, not cartoonish.

```html
<!DOCTYPE html>
<html lang="en">
<head>
<meta charset="utf-8">
<title>Vardel GreenWorks – Business Card</title>
<link href="https://fonts.googleapis.com/css2?family=Hanken+Grotesk:wght@400;500;700&display=swap" rel="stylesheet">
<style>
  :root {
    --bg: #e3e5e3;
    --card-white: #f3f3f3;
    --card-white-shade: #e2e2e2;
    --green: #62a53b;
    --green-deep: #56963a;
    --teal: #1f7fa0;
    --ink: #555a5c;
    --service-ink: #e9efe4;
    --brand-green: #5a9e34;
    --brand-light: #ececec;
  }
  * { box-sizing: border-box; margin: 0; padding: 0; }
  html, body { width: 1200px; height: 1200px; overflow: hidden; }
  body {
    background: var(--bg);
    font-family: "Hanken Grotesk", Arial, sans-serif;
    position: relative;
  }
  .card {
    position: absolute;
    left: 255px;
    width: 729px;
    height: 416px;
    border-radius: 4px;
    box-shadow: 0 6px 18px rgba(0,0,0,0.18);
  }
  .card-front {
    top: 134px;
    background: linear-gradient(160deg, var(--card-white) 0%, var(--card-white-shade) 100%);
  }
  .card-back {
    top: 611px;
    background: linear-gradient(160deg, var(--green-deep) 0%, var(--green) 100%);
  }
  .holder-name {
    position: absolute; left: 51px; top: 42px;
    font-size: 36px; font-weight: 700; color: var(--teal); letter-spacing: 0.3px;
  }
  .holder-title {
    position: absolute; left: 51px; top: 87px;
    font-size: 21px; color: var(--ink);
  }
  .address {
    position: absolute; left: 51px; top: 182px;
    font-size: 21.5px; line-height: 27px; color: var(--ink);
  }
  .contact-list {
    position: absolute; left: 51px; top: 256px; list-style: none;
  }
  .contact-list li {
    display: flex; align-items: center; height: 29.3px;
    font-size: 21.5px; color: var(--ink);
  }
  .contact-list svg { width: 16px; height: 16px; margin-right: 8px; fill: var(--teal); flex: none; }
  .brand {
    position: absolute; display: flex; align-items: center;
    font-weight: 700; white-space: nowrap;
  }
  .brand-front { right: 50px; bottom: 50px; font-size: 22px; color: var(--brand-green); }
  .brand-front .brand-dot { width: 40px; height: 40px; border-radius: 50%; background: var(--teal); margin-right: 10px; }
  .brand-back { right: 46px; bottom: 52px; font-size: 36px; color: var(--brand-light); }
  .brand-back .brand-dot { width: 68px; height: 68px; border-radius: 50%; background: var(--teal); margin-right: 16px; }
  .service-list {
    position: absolute; left: 46px; top: 40px; list-style: none;
  }
  .service-list li {
    display: flex; align-items: center; height: 31px;
    font-size: 22px; color: var(--service-ink);
  }
  .service-list li::before {
    content: ""; width: 8px; height: 8px; border-radius: 50%;
    background: var(--service-ink); margin-right: 6px;
  }
</style>
</head>
<body>
  <section class="card card-front">
    <h1 class="holder-name">Marcus T. Ellery, PE</h1>
    <p class="holder-title">President, Principle Engineer</p>
    <p class="address">4810 Ridgeline Parkway, Ste<br>210 Marlow, TN 37999</p>
    <ul class="contact-list">
      <li><svg viewBox="0 0 16 16"><path d="M3.5 1.5l2.5 3-1.5 1.8c.8 1.8 2.4 3.4 4.2 4.2l1.8-1.5 3 2.5-1.6 2.5C6.8 13.6 2.4 9.2 1 3.1z"/></svg>888-555-0143</li>
      <li><svg viewBox="0 0 16 16"><path d="M4 0h8a1.5 1.5 0 0 1 1.5 1.5v13A1.5 1.5 0 0 1 12 16H4a1.5 1.5 0 0 1-1.5-1.5v-13A1.5 1.5 0 0 1 4 0zm0 2v10.5h8V2zm4 11.3a.9.9 0 1 0 0 1.8.9.9 0 0 0 0-1.8z"/></svg>423-555-0187</li>
      <li><svg viewBox="0 0 16 16"><path d="M1 3h14v10H1zm1.5 1.4V5l5.5 4 5.5-4v-.6z"/></svg>mellery@vardelgw.example</li>
      <li><svg viewBox="0 0 16 16"><path d="M8 1a7 7 0 1 0 0 14A7 7 0 0 0 8 1zm0 1.5c.9.9 1.6 2.4 1.8 4.5H6.2C6.4 4.9 7.1 3.4 8 2.5zM2.6 7h2.1c.1-1.7.5-3.1 1.1-4.1A5.5 5.5 0 0 0 2.6 7zm8.7 0h2.1a5.5 5.5 0 0 0-3.2-4.1c.6 1 1 2.4 1.1 4.1zM2.6 9a5.5 5.5 0 0 0 3.2 4.1c-.6-1-1-2.4-1.1-4.1zm3.6 0c.2 2.1.9 3.6 1.8 4.5.9-.9 1.6-2.4 1.8-4.5zm5.1 0c-.1 1.7-.5 3.1-1.1 4.1A5.5 5.5 0 0 0 13.4 9z"/></svg>www.vardelgw.example</li>
    </ul>
    <div class="brand brand-front"><span class="brand-dot"></span>Vardel GreenWorks</div>
  </section>

  <section class="card card-back">
    <ul class="service-list">
      <li>LFG Engineering and Design</li>
      <li>GCCS Planning and Operational Cousulting</li>
      <li>Compliance Monitoring and Reporting</li>
      <li>Routine Operations &amp; Maintenance</li>
      <li>Nonroutine O&amp;M</li>
      <li>Construction Management</li>
      <li>Construction QA</li>
      <li>GCCS Construction</li>
    </ul>
    <div class="brand brand-back"><span class="brand-dot"></span>Vardel GreenWorks</div>
  </section>
</body>
</html>
```